Dental 2 practice oudoor signs

I need 2 high quality practice signs designed
sign 1 ( 1.6m high by 0.8m wide)
sign 2 ( sign 1.05m high by 0.80m wide)

I had sign 1 displayed before which i have attached but it doest look as professional now. We are a multi award winning dental clinic. Both signs will be printed on dibond and be at a 45 degree to each other so that the person walking past will only see one sign, unless he walks in the opposite direction. Here is the brief of sign 1 and sign 2 but feel free to diverse away from the brief and do something differet

Sign 1
Merlow Dental, Implant & Orthodontic Centre

Size of sign 1600 Height by 800 WIde
website: www.merlowdentalsurgery.example
Sign text

Multi-Award Winning
Centre of Excellence

Dental Implants from £ 38.23/mo
Clearfitra Braces from £ 29.23/mo
Dental Veneers from £11.13/mo
Smile Makeovers from £34.13/mo
Specialist Orthodontics from £29.23/mo
Facial Aesthetics from £22.16/mo

020 7395 0618
www.merlowdentalsurgery.example

Each of the above treatements should be also represented graphically so the sign is very colorful and draws your attention but gives a quality feel about it
You can find graphics wherever you need to, to advertise the services

Sign 2.
Use any detail you wish from sign 1 but i definately want
Multi-Award Winning on both signs

Target Market(s)

Passers by who are driving past dental practice or pedestrians who are walking past practice

Industry/Entity Type

Dental Clinic

Colors

Designer to choose colors to be used in the design.

Requirements
Must have
• See brief

```html
<!DOCTYPE html>
<html lang="en">
<head>
<meta charset="utf-8">
<title>Merlow Dental – Practice Signs</title>
<link rel="stylesheet" href="https://fonts.googleapis.com/css2?family=Libre+Baskerville:wght@700&family=Libre+Bodoni:wght@700&family=Raleway:wght@300;400&family=Questrial&display=swap">
<style>
  :root{
    --navy:#0c2a52;
    --navy-deep:#071d3d;
    --ink:#10264a;
    --teal:#1a8db5;
    --teal-light:#7cc4dc;
    --gold:#f2a81d;
    --paper-top:#d4d1c8;
    --paper-mid:#e9e8e3;
    --paper-low:#cfcdc6;
    --white:#ffffff;
    --label-grey:#6b6b6b;
  }
  *{box-sizing:border-box;margin:0;padding:0}
  html,body{width:1200px;height:1200px;overflow:hidden;background:var(--white)}
  body{position:relative;font-family:"Raleway",sans-serif}

  .sign{position:absolute;overflow:hidden;
    background:linear-gradient(160deg,var(--paper-top) 0%,var(--paper-mid) 45%,var(--paper-low) 100%)}
  .sign--tall{left:18px;top:20px;width:569px;height:1138px}
  .sign--short{left:614px;top:20px;width:568px;height:746px}

  .sign-caption{position:absolute;font-family:"Questrial",sans-serif;font-size:19px;color:var(--label-grey);letter-spacing:.5px}

  /* brand */
  .brand{position:absolute;display:flex;align-items:center;gap:9px;width:200px}
  .brand__dot{width:34px;height:34px;border-radius:50%;background:var(--navy);flex:none}
  .brand__name{font-family:"Libre Baskerville",serif;font-weight:700;color:var(--navy);line-height:1.15;white-space:nowrap}
  .brand__name span{display:block}
  .brand__main{font-size:14px;letter-spacing:1px}
  .brand__sub{font-size:9px;letter-spacing:4.5px;margin-top:4px;color:var(--teal)}
  .divider{position:absolute;width:1px;background:rgba(12,42,82,.25)}
  .headline{position:absolute;font-family:"Libre Baskerville",serif;font-weight:700;font-size:23px;line-height:31px;color:var(--ink);letter-spacing:.5px}
  .headline .amp{color:var(--teal)}

  .portrait{position:absolute;
    background:radial-gradient(ellipse 48% 46% at 52% 42%,#e9c0a4 0%,#c99a7c 35%,rgba(140,98,70,.75) 60%,rgba(190,184,178,0) 100%)}

  .swoosh{position:absolute;left:0;top:0}

  /* treatments */
  .treatment{position:absolute;left:0;width:100%;height:116px}
  .treatment__name{position:absolute;left:170px;width:244px;top:21px;text-align:right;
    font-family:"Raleway",sans-serif;font-weight:400;font-size:19px;line-height:20px;color:var(--ink);text-transform:uppercase}
  .treatment__name .thin{font-weight:300}
  .price{position:absolute;left:252px;top:61px;width:170px;height:35px;background:var(--teal);
    clip-path:polygon(0 0,95.5% 0,100% 50%,95.5% 100%,0 100%);
    color:var(--white);display:flex;align-items:center;justify-content:flex-end;padding-right:14px;gap:5px;white-space:nowrap}
  .price__from{font-family:"Raleway",sans-serif;font-weight:400;font-size:15px}
  .price__amount{font-family:"Libre Bodoni",serif;font-weight:700;font-size:21px}
  .treatment__art{position:absolute;left:424px;top:0;width:116px;height:116px;border-radius:50%;
    border:4px solid rgba(255,255,255,.75);box-shadow:0 0 0 2px rgba(160,160,160,.35)}
  .art--implant{background:radial-gradient(circle at 50% 60%,#f4f4f2 0%,#f1d2c8 45%,#8fc3d6 100%)}
  .art--aligner{background:radial-gradient(circle at 55% 55%,#fbf4ef 0%,#e7a99a 50%,#d98a80 100%)}
  .art--veneer{background:radial-gradient(circle at 60% 50%,#eeeeee 0%,#e98e9a 55%,#d6546a 100%)}
  .art--smile{background:radial-gradient(circle at 50% 50%,#fbfbf9 0%,#e69a9a 45%,#b5384a 100%)}
  .art--ortho{background:radial-gradient(circle at 60% 50%,#f0c9ad 0%,#d9a98a 50%,#6fb0d0 100%)}

  /* contact band */
  .phone-icon{position:absolute;width:44px;height:44px}
  .phone-number{position:absolute;font-family:"Libre Bodoni",serif;font-weight:700;font-size:33px;color:var(--white);text-align:center;white-space:nowrap;letter-spacing:-.5px}
  .web-bar{position:absolute;background:var(--teal);color:var(--white);font-family:"Questrial",sans-serif;font-size:15.5px;font-weight:700;display:flex;align-items:center;justify-content:center;letter-spacing:.2px;white-space:nowrap}
  .award-mark{position:absolute;border-radius:50%;
    background:radial-gradient(circle at 50% 42%,#ffe08a 0%,#e9a72a 40%,rgba(160,110,20,.6) 70%,rgba(7,29,61,0) 72%)}
  .award-text{position:absolute;font-family:"Questrial",sans-serif;font-size:21px;line-height:21px;color:var(--gold)}
</style>
</head>
<body>

<!-- Sign 01 -->
<section class="sign sign--tall" aria-label="Sign 01">
  <div class="brand" style="left:30px;top:82px">
    <div class="brand__dot"></div>
    <div class="brand__name"><span class="brand__main">MERLOW DENTAL</span><span class="brand__sub">SURGERY</span></div>
  </div>
  <div class="divider" style="left:247px;top:44px;height:112px"></div>
  <h1 class="headline" style="left:263px;top:40px">DENTAL,<br>IMPLANT <span class="amp">&amp;</span><br>ORTHODONTIC<br>CENTRE</h1>

  <div class="portrait" role="img" aria-label="Smiling woman holding a red apple" style="left:0;top:220px;width:400px;height:600px"></div>

  <svg class="swoosh" width="569" height="1138" viewBox="0 0 569 1138" aria-hidden="true">
    <defs>
      <linearGradient id="tealBandA" x1="0" y1="0" x2="1" y2="0">
        <stop offset="0" stop-color="#1a8db5"/><stop offset=".5" stop-color="#86c9df"/><stop offset="1" stop-color="#1a8db5"/>
      </linearGradient>
      <linearGradient id="navyA" x1="0" y1="0" x2="0" y2="1">
        <stop offset="0" stop-color="#0c2a52"/><stop offset="1" stop-color="#071d3d"/>
      </linearGradient>
    </defs>
    <path d="M0,866 C180,800 420,790 569,632 L569,700 C420,830 180,840 0,900 Z" fill="#ffffff"/>
    <path d="M0,892 C180,835 410,830 569,676 L569,890 C300,890 120,900 0,980 Z" fill="url(#tealBandA)"/>
    <path d="M0,980 C120,912 260,890 569,890 L569,1138 L0,1138 Z" fill="url(#navyA)"/>
  </svg>

  <div class="treatment" style="top:196px">
    <div class="treatment__name"><span class="thin">Dental</span><br>Implants</div>
    <div class="price"><span class="price__from">from</span><span class="price__amount">£ 38.23/mo</span></div>
    <div class="treatment__art art--implant" role="img" aria-label="Dental implant between natural teeth"></div>
  </div>
  <div class="treatment" style="top:318px">
    <div class="treatment__name"><span class="thin">Clearfitra</span><br>Braces</div>
    <div class="price"><span class="price__from">from</span><span class="price__amount">£ 29.23/mo</span></div>
    <div class="treatment__art art--aligner" role="img" aria-label="Clear aligner being fitted to teeth"></div>
  </div>
  <div class="treatment" style="top:440px">
    <div class="treatment__name"><span class="thin">Dental</span><br>Veneers</div>
    <div class="price"><span class="price__from">from</span><span class="price__amount">£11.13/mo</span></div>
    <div class="treatment__art art--veneer" role="img" aria-label="Porcelain veneer placed on a tooth"></div>
  </div>
  <div class="treatment" style="top:562px">
    <div class="treatment__name"><span class="thin">Smile</span><br>Makeovers</div>
    <div class="price"><span class="price__from">from</span><span class="price__amount">£34.13/mo</span></div>
    <div class="treatment__art art--smile" role="img" aria-label="Close-up of a bright smile"></div>
  </div>
  <div class="treatment" style="top:684px">
    <div class="treatment__name"><span class="thin">Specialist</span><br>Orthodontics</div>
    <div class="price"><span class="price__from">from</span><span class="price__amount">£29.23/mo</span></div>
    <div class="treatment__art art--ortho" role="img" aria-label="Patient having a dental check-up"></div>
  </div>

  <svg class="phone-icon" style="left:160px;top:966px" viewBox="0 0 44 44" aria-hidden="true">
    <path d="M10 6 L16 6 L19 14 L15 17 C17 22 21 26 26 28 L29 24 L37 27 L37 33 C37 36 34 38 31 37 C19 34 9 24 6 12 C5 9 7 6 10 6 Z" fill="#1a8db5"/>
    <path d="M24 8 A12 12 0 0 1 35 19" fill="none" stroke="#1a8db5" stroke-width="3" stroke-linecap="round"/>
    <path d="M24 14 A6 6 0 0 1 29 19" fill="none" stroke="#1a8db5" stroke-width="3" stroke-linecap="round"/>
  </svg>
  <div class="phone-number" style="left:36px;width:300px;top:1006px">020 7395 0618</div>
  <div class="web-bar" style="left:47px;top:1044px;width:275px;height:34px">www.merlowdentalsurgery.example</div>

  <div class="award-mark" role="img" aria-label="Gold trophy within a laurel wreath" style="left:382px;top:916px;width:120px;height:120px"></div>
  <div class="award-text" style="left:330px;width:226px;top:1040px;text-align:center">Multi-Award<br>Winning<br>Centre of Excellence</div>
</section>
<div class="sign-caption" style="left:514px;top:1164px">Sign 01</div>

<!-- Sign 02 -->
<section class="sign sign--short" aria-label="Sign 02">
  <div class="brand" style="left:30px;top:74px">
    <div class="brand__dot"></div>
    <div class="brand__name"><span class="brand__main">MERLOW DENTAL</span><span class="brand__sub">SURGERY</span></div>
  </div>
  <div class="divider" style="left:248px;top:36px;height:116px"></div>
  <h1 class="headline" style="left:264px;top:32px">DENTAL,<br>IMPLANT <span class="amp">&amp;</span><br>ORTHODONTIC<br>CENTRE</h1>

  <div class="portrait" role="img" aria-label="Smiling woman holding a red apple" style="left:10px;top:156px;width:330px;height:400px"></div>

  <svg class="swoosh" width="568" height="746" viewBox="0 0 568 746" aria-hidden="true">
    <defs>
      <linearGradient id="tealBandB" x1="0" y1="0" x2="1" y2="0">
        <stop offset="0" stop-color="#1a8db5"/><stop offset=".5" stop-color="#86c9df"/><stop offset="1" stop-color="#1a8db5"/>
      </linearGradient>
      <linearGradient id="navyB" x1="0" y1="0" x2="0" y2="1">
        <stop offset="0" stop-color="#0c2a52"/><stop offset="1" stop-color="#071d3d"/>
      </linearGradient>
    </defs>
    <path d="M0,528 C200,440 420,470 568,292 L568,360 C420,500 200,480 0,556 Z" fill="#ffffff"/>
    <path d="M0,545 C200,480 420,505 568,345 L568,568 C250,568 100,590 0,644 Z" fill="url(#tealBandB)"/>
    <path d="M0,644 C100,590 250,568 568,568 L568,746 L0,746 Z" fill="url(#navyB)"/>
  </svg>

  <div class="treatment" style="top:178px">
    <div class="treatment__name"><span class="thin">Dental</span><br>Implants</div>
    <div class="price"><span class="price__from">from</span><span class="price__amount">£ 38.23/mo</span></div>
    <div class="treatment__art art--implant" role="img" aria-label="Dental implant between natural teeth"></div>
  </div>
  <div class="treatment" style="top:298px">
    <div class="treatment__name"><span class="thin">Clearfitra</span><br>Braces</div>
    <div class="price"><span class="price__from">from</span><span class="price__amount">£ 29.23/mo</span></div>
    <div class="treatment__art art--aligner" role="img" aria-label="Clear aligner being fitted to teeth"></div>
  </div>
  <div class="treatment" style="top:422px">
    <div class="treatment__name"><span class="thin">Dental</span><br>Veneers</div>
    <div class="price"><span class="price__from">from</span><span class="price__amount">£11.13/mo</span></div>
    <div class="treatment__art art--veneer" role="img" aria-label="Porcelain veneer placed on a tooth"></div>
  </div>

  <svg class="phone-icon" style="left:132px;top:618px" viewBox="0 0 44 44" aria-hidden="true">
    <path d="M10 6 L16 6 L19 14 L15 17 C17 22 21 26 26 28 L29 24 L37 27 L37 33 C37 36 34 38 31 37 C19 34 9 24 6 12 C5 9 7 6 10 6 Z" fill="#1a8db5"/>
    <path d="M24 8 A12 12 0 0 1 35 19" fill="none" stroke="#1a8db5" stroke-width="3" stroke-linecap="round"/>
    <path d="M24 14 A6 6 0 0 1 29 19" fill="none" stroke="#1a8db5" stroke-width="3" stroke-linecap="round"/>
  </svg>
  <div class="phone-number" style="left:7px;width:300px;top:650px">020 7395 0618</div>
  <div class="web-bar" style="left:26px;top:688px;width:260px;height:32px;font-size:14.5px">www.merlowdentalsurgery.example</div>

  <div class="award-mark" role="img" aria-label="Gold trophy within a laurel wreath" style="left:302px;top:610px;width:108px;height:108px"></div>
  <div class="award-text" style="left:416px;top:622px">Multi-Award<br>Winning<br>Centre of<br>Excellence</div>
</section>
<div class="sign-caption" style="left:1108px;top:776px">Sign 02</div>

</body>
</html>
```